MOSSLANTERNWORKS-BUSINESS!!!CARDS

HELLO! GOOD LUCK!
--------------------------------------------------------------------------

SUPPLIED: AI File (business card, as I have designed so far)

PLEASE KEEP: Logo in Header*

PLEASE RETAIN: Content as per AI File

* If you're keen, feel free to change things up, no problem with that, however I suggest you also include a version which
has the logo in the header. Thankyou!

----------------------------------------------------------------

Extra Info:

new website in development right now, however you can see the style of what we used to do.
time to turn the corner!!!

I will respond with advice & or suggestions for every entry.

Also looking for new freelance designers for exxxxtra work CHEERS!

```html
<!DOCTYPE html>
<html lang="en">
<head>
<meta charset="utf-8">
<title>MossLanternWorks – Business Card</title>
<link href="https://fonts.googleapis.com/css2?family=Nunito:wght@400;700;800&display=swap" rel="stylesheet">
<style>
  :root {
    --brand-blue: #1ea4dd;
    --accent-gold: #e6a92a;
    --ink-grey: #6b6b6b;
    --card-edge: #e4e4e4;
    --paper: #ffffff;
  }
  html, body {
    margin: 0;
    padding: 0;
    width: 1084px;
    height: 1200px;
    overflow: hidden;
    background: var(--paper);
    font-family: "Nunito", sans-serif;
  }
  .canvas {
    position: relative;
    width: 1084px;
    height: 1200px;
  }
  .card {
    position: absolute;
    left: 90px;
    width: 898px;
    background: var(--paper);
    border: 2px solid var(--card-edge);
    box-sizing: border-box;
  }
  .card--front { top: 79px; height: 511px; }
  .card--back { top: 612px; height: 515px; }

  /* Front */
  .brand {
    position: absolute;
    top: 52px;
    right: 58px;
    display: flex;
    align-items: center;
    gap: 16px;
  }
  .brand__dot {
    width: 64px;
    height: 64px;
    border: 3px solid var(--accent-gold);
    border-radius: 50%;
    box-sizing: border-box;
  }
  .brand__name {
    font-size: 44px;
    font-weight: 700;
    color: var(--brand-blue);
    letter-spacing: -0.5px;
    line-height: 1;
  }
  .person {
    position: absolute;
    left: 66px;
    top: 172px;
  }
  .person__name {
    margin: 0;
    font-size: 36px;
    font-weight: 800;
    color: var(--brand-blue);
    line-height: 1;
  }
  .person__role {
    margin: 14px 0 0;
    font-size: 22px;
    color: var(--ink-grey);
  }
  .contact {
    position: absolute;
    left: 66px;
    top: 312px;
    margin: 0;
    padding: 0;
    list-style: none;
    font-size: 23px;
    color: var(--ink-grey);
  }
  .contact__item {
    display: block;
    line-height: 1;
    padding-bottom: 8px;
    margin-bottom: 12px;
  }
  .contact__item--underlined {
    border-bottom: 3px solid var(--brand-blue);
  }
  .contact__item--phone { width: 178px; }
  .contact__item--email { width: 325px; }
  .contact__item--address { width: 520px; }
  .contact__item--office { padding-left: 6px; border: none; }

  /* Back */
  .services {
    position: absolute;
    top: 112px;
    left: 0;
    right: 0;
    text-align: center;
    font-size: 27px;
    color: var(--ink-grey);
  }
  .services__line {
    display: inline-block;
    margin: 0;
    line-height: 1.2;
  }
  .services__line--primary {
    padding: 0 14px 8px;
    border-bottom: 3px solid var(--brand-blue);
  }
  .services__line--secondary {
    display: block;
    margin-top: 8px;
  }
  .back-mark {
    position: absolute;
    top: 293px;
    left: 409px;
    width: 80px;
    height: 80px;
    border: 3px solid var(--accent-gold);
    border-radius: 50%;
    box-sizing: border-box;
  }
  .web-band {
    position: absolute;
    left: -2px;
    right: -2px;
    top: 406px;
    height: 40px;
    display: flex;
    align-items: center;
  }
  .web-band__bar {
    height: 27px;
    background: var(--brand-blue);
  }
  .web-band__bar--left { width: 200px; }
  .web-band__bar--right { width: 188px; margin-left: auto; }
  .web-band__url {
    flex: 1;
    text-align: center;
    font-size: 31px;
    font-weight: 800;
    color: var(--brand-blue);
    letter-spacing: 0.5px;
  }
</style>
</head>
<body>
<main class="canvas">
  <section class="card card--front" aria-label="Card front">
    <div class="brand">
      <span class="brand__dot"></span>
      <span class="brand__name">MossLanternWorks</span>
    </div>
    <div class="person">
      <h1 class="person__name">Clara Voss</h1>
      <p class="person__role">Director</p>
    </div>
    <ul class="contact">
      <li class="contact__item contact__item--underlined contact__item--phone">040 517 32 90</li>
      <li class="contact__item contact__item--underlined contact__item--email">clara@mosslanternworks.com</li>
      <li class="contact__item contact__item--underlined contact__item--address">LVL 14, TWR III, 88 HARBOUR LN, SYDNEY 2000</li>
      <li class="contact__item contact__item--office">(02) 8114 6720</li>
    </ul>
  </section>

  <section class="card card--back" aria-label="Card back">
    <div class="services">
      <p class="services__line services__line--primary">Fresh Updates , Design &amp; Development</p>
      <p class="services__line services__line--secondary">TABLET Lounge - Project Management APPS</p>
    </div>
    <span class="back-mark"></span>
    <div class="web-band">
      <span class="web-band__bar web-band__bar--left"></span>
      <span class="web-band__url">www.mosslanternworks.com</span>
      <span class="web-band__bar web-band__bar--right"></span>
    </div>
  </section>
</main>
</body>
</html>
```